Pemberly & Associates Tax Services

Need an eye catching advertisement/lead generating design for prospects interesting in professional tax planning and tax preparation services. Ideas for
Sample Advertising Language is below:

We are accepting new clients!!
We are affordable and have over 20 years of experience serving the tax needs of our clientele.

Here are a few reasons you may want to contact us:

1. You want to learn how to maximize business deductions
2. You’re a high-income earner and want to learn ways to pay less in taxes
3. You have an interest in starting a business
4. You want to maximize rental property deductions
5. You have questions about maintaining a home office
6. You want to be updated periodically on tax law changes and tax planning strategies
7. You want to be represented by a tax expert before the FRB if you are subject to an audit

References available upon request.

Target Market(s)

Individuals, small businesses and startup business

Industry/Entity Type

Tax and Accounting Industry

Requirements
Nice to have
• Would like to develop a marketing campaign that can be used periodically to digitally generate leads, build email contact list of prospective clients who want to receive tax updates.

```html
<!DOCTYPE html>
<html lang="en">
<head>
<meta charset="utf-8">
<title>Pemberly &amp; Associates Tax Services – Flyer</title>
<link rel="stylesheet" href="https://fonts.googleapis.com/css2?family=Montserrat:wght@400;500;700;800&display=swap">
<style>
  :root {
    --brand-blue: #2a5e9e;
    --brand-green: #2f9a58;
    --ink: #3d3d3d;
    --paper: #ffffff;
    --rule: #cfd4d8;
    --badge-fill: #d9dcdf;
    --agent-grey: #6f6d67;
  }
  * { margin: 0; padding: 0; box-sizing: border-box; }
  html, body { width: 915px; height: 1200px; overflow: hidden; }
  body {
    position: relative;
    background: var(--paper);
    font-family: "Montserrat", Arial, sans-serif;
    color: var(--ink);
  }
  .abs { position: absolute; }

  .hero-photo {
    left: 300px; top: 0; width: 615px; height: 534px;
    background:
      linear-gradient(to bottom, rgba(255,255,255,0) 70%, rgba(240,242,244,0.6) 100%),
      linear-gradient(to right, #ffffff 0%, #eef1f3 20%, #c3ccd5 42%, #66727f 66%, #2f3744 88%, #3a3f47 100%);
  }
  .lower-backdrop {
    left: 0; top: 561px; width: 500px; height: 527px;
    background: linear-gradient(160deg, #ffffff 0%, #f3f4f5 40%, #e9eaec 80%, #f6f6f6 100%);
  }

  .band-blue  { left: 0; top: 534px; width: 915px; height: 14px; background: var(--brand-blue); }
  .band-green { left: 0; top: 548px; width: 915px; height: 13px; background: var(--brand-green); }

  .brand { left: 44px; top: 52px; display: flex; align-items: center; gap: 14px; }
  .brand-dot { width: 60px; height: 60px; border-radius: 50%; background: var(--brand-blue); }
  .brand-name { font-weight: 700; font-size: 23px; line-height: 27px; color: var(--brand-blue); }

  .headline {
    left: 47px; top: 178px; font-weight: 800; font-size: 39px; line-height: 41px; letter-spacing: 0.3px;
  }
  .headline .blue { color: var(--brand-blue); }
  .headline .green { color: var(--brand-green); }
  .headline .amp { font-weight: 500; color: var(--brand-blue); }

  .intro { left: 48px; top: 598px; width: 380px; font-size: 20px; line-height: 24px; }
  .reasons { left: 48px; top: 669px; width: 412px; list-style: none; }
  .reasons li {
    position: relative; padding-left: 36px; font-size: 17.5px; line-height: 21.7px; margin-bottom: 4.6px;
  }
  .reasons li svg { position: absolute; left: 0; top: 2px; width: 18px; height: 18px; }

  .desk-photo {
    left: 520px; top: 596px; width: 337px; height: 159px;
    border: 1px solid var(--brand-green);
    background: var(--paper);
  }
  .desk-photo .fill {
    position: absolute; inset: 5px;
    background: linear-gradient(135deg, #e9ecef 0%, #f4f4f2 35%, #c9a77e 60%, #8a8d90 80%, #d8dde2 100%);
  }
  .pitch {
    left: 520px; top: 766px; width: 380px; font-size: 24.5px; line-height: 26.5px; color: var(--brand-blue);
  }
  .pitch strong { color: var(--brand-green); font-weight: 700; }

  .credential { left: 523px; top: 894px; display: flex; align-items: center; gap: 8px; }
  .credential-badge { width: 128px; height: 68px; background: var(--badge-fill); }
  .credential-title { font-weight: 800; font-size: 28.5px; line-height: 31px; color: var(--agent-grey); letter-spacing: 0.5px; }
  .divider { left: 520px; top: 982px; width: 337px; height: 1px; background: var(--rule); }
  .call-label { left: 521px; top: 996px; font-size: 22px; color: var(--brand-blue); }
  .phone { left: 517px; top: 1018px; font-size: 39px; font-weight: 800; color: var(--brand-green); letter-spacing: 0.5px; }

  .banner { left: 0; top: 1088px; width: 915px; height: 32px; background: var(--brand-green); }
  .banner-rule { left: 0; top: 1120px; width: 915px; height: 7px; background: var(--brand-blue); }
  .banner-text { left: 48px; top: 1087px; font-size: 29px; font-weight: 700; color: var(--paper); line-height: 34px; }

  .contact { top: 1142px; display: flex; gap: 10px; color: var(--brand-blue); font-size: 19px; line-height: 21px; }
  .contact svg { flex: none; margin-top: 2px; }
  .contact.address { left: 48px; }
  .contact.email { left: 440px; }
</style>
</head>
<body>

  <div class="abs hero-photo" role="img" aria-label="Photo of two businessmen in suits reviewing charts on a laptop at an office table"></div>
  <div class="abs band-blue"></div>
  <div class="abs band-green"></div>
  <div class="abs lower-backdrop" role="img" aria-label="Faint washed-out photo of an office meeting behind the list"></div>

  <div class="abs brand">
    <span class="brand-dot"></span>
    <span class="brand-name">Pemberly &amp; Associates<br>Tax Services</span>
  </div>

  <h1 class="abs headline">
    <span class="blue">TAX PLANNING</span> <span class="amp">&amp;</span><br>
    <span class="green">TAX PREPARATION<br>SERVICES</span>
  </h1>

  <p class="abs intro">Here are a few reasons you may<br>want to contact us:</p>

  <ul class="abs reasons">
    <li><svg viewBox="0 0 18 18"><circle cx="9" cy="9" r="7.5" fill="none" stroke="var(--brand-blue)" stroke-width="1.6"/><path d="M5 9.2l2.8 2.8L13.5 5.5" fill="none" stroke="var(--brand-green)" stroke-width="2"/></svg>You want to learn how to maximize business deductions</li>
    <li><svg viewBox="0 0 18 18"><circle cx="9" cy="9" r="7.5" fill="none" stroke="var(--brand-blue)" stroke-width="1.6"/><path d="M5 9.2l2.8 2.8L13.5 5.5" fill="none" stroke="var(--brand-green)" stroke-width="2"/></svg>You’re a high-income earner and want to learn ways to pay less in taxes</li>
    <li><svg viewBox="0 0 18 18"><circle cx="9" cy="9" r="7.5" fill="none" stroke="var(--brand-blue)" stroke-width="1.6"/><path d="M5 9.2l2.8 2.8L13.5 5.5" fill="none" stroke="var(--brand-green)" stroke-width="2"/></svg>You have an interest in starting a<br>business</li>
    <li><svg viewBox="0 0 18 18"><circle cx="9" cy="9" r="7.5" fill="none" stroke="var(--brand-blue)" stroke-width="1.6"/><path d="M5 9.2l2.8 2.8L13.5 5.5" fill="none" stroke="var(--brand-green)" stroke-width="2"/></svg>You want to maximize rental property deductions</li>
    <li><svg viewBox="0 0 18 18"><circle cx="9" cy="9" r="7.5" fill="none" stroke="var(--brand-blue)" stroke-width="1.6"/><path d="M5 9.2l2.8 2.8L13.5 5.5" fill="none" stroke="var(--brand-green)" stroke-width="2"/></svg>You have questions about maintaining a home office</li>
    <li><svg viewBox="0 0 18 18"><circle cx="9" cy="9" r="7.5" fill="none" stroke="var(--brand-blue)" stroke-width="1.6"/><path d="M5 9.2l2.8 2.8L13.5 5.5" fill="none" stroke="var(--brand-green)" stroke-width="2"/></svg>You want to be updated periodically on tax law changes and tax planning strategies</li>
    <li><svg viewBox="0 0 18 18"><circle cx="9" cy="9" r="7.5" fill="none" stroke="var(--brand-blue)" stroke-width="1.6"/><path d="M5 9.2l2.8 2.8L13.5 5.5" fill="none" stroke="var(--brand-green)" stroke-width="2"/></svg>You want to be represented by a tax expert before the FRB if you are subject to an audit</li>
  </ul>

  <div class="abs desk-photo">
    <div class="fill" role="img" aria-label="Photo of hands using a calculator over tax paperwork on a desk"></div>
  </div>

  <p class="abs pitch">We are <strong>affordable</strong> and have<br>over <strong>20 years of experience</strong><br><strong>serving</strong> the tax needs of<br>our clientele.</p>

  <div class="abs credential">
    <div class="credential-badge"></div>
    <div class="credential-title">ENROLLED<br>AGENT</div>
  </div>

  <div class="abs divider"></div>
  <p class="abs call-label">Call us for an appointment</p>
  <p class="abs phone">(555) 014-2287</p>

  <div class="abs banner"></div>
  <div class="abs banner-rule"></div>
  <p class="abs banner-text">We are accepting new clients!!</p>

  <div class="abs contact address">
    <svg width="12" height="17" viewBox="0 0 12 17"><path d="M6 0a6 6 0 0 0-6 6c0 4.5 6 11 6 11s6-6.5 6-11a6 6 0 0 0-6-6z" fill="var(--brand-green)"/><circle cx="6" cy="6" r="2.3" fill="#fff"/></svg>
    <span>418 Alder Creek Rd., Suite 210,<br>Fairmont, CA 95000</span>
  </div>
  <div class="abs contact email">
    <svg width="16" height="12" viewBox="0 0 16 12"><rect width="16" height="12" rx="1" fill="var(--brand-green)"/><path d="M1 1.5l7 5 7-5" fill="none" stroke="#fff" stroke-width="1.4"/></svg>
    <span>hello@pemberlytax.com</span>
  </div>

</body>
</html>
```